Logo + Label Design (Men’s Grooming Brand & Product Packaging)

Design a logo and 2 oz pomade label for Brant, a modern men’s grooming brand focused on clean, high-quality, natural ingredients. The design should establish a bold, masculine, minimalist identity that can later extend to products like shaving gel and body wash.

Key Requirements

Create a primary logo for “Brant” and a core label for the 2 oz pomade jar (screw-top).

Use a clean, modern style — masculine, confident, and approachable (think Wendel’s, Valto, Northfield Mill).

Design for 1–2 color screen printing on solid jar colors (white, black, or navy).

Avoid gradients, foil, or embossing. Must work in black & white.

Provide: vector logo, mockup of the 2 oz jar, color palette (CMYK/RGB/HEX), and font specs.

Winning design may lead to future projects (body wash, shave gel, skincare lines).

Font styles to use
Other font styles liked:
• We like the fonts and design concept in the attached mockup.

Requirements
Should not have
• We want to avoid too much writing or busy designs. We want to avoid having graphics/illustrations embedded in the logo if they will cause the brand to look less classy or sophisticated. We also want the design to look simple and all-American (e.g. Pellham and Stroud, Tall Pine, The BRIM, etc). We’d like to give a Kessler & Dunmore vibe that feels classy and high end.

```html
<!DOCTYPE html>
<html lang="en">
<head>
<meta charset="UTF-8">
<title>Brant Hair Pomade – 2 oz Jar Label</title>
<link rel="stylesheet" href="https://fonts.googleapis.com/css2?family=Playfair+Display:wght@800&family=Montserrat:wght@500;700&display=swap">
<style>
  :root {
    --page-bg: #f6f4f0;
    --label-white: #ffffff;
    --label-edge: #e4e1dc;
    --ink: #111111;
  }
  * { margin: 0; padding: 0; box-sizing: border-box; }
  html, body {
    width: 1200px;
    height: 1200px;
    overflow: hidden;
    background: var(--page-bg);
  }
  .canvas {
    position: relative;
    width: 1200px;
    height: 1200px;
  }
  .lid-label {
    position: absolute;
    left: 290px;
    top: 50px;
    width: 620px;
    height: 620px;
    border-radius: 50%;
    background: var(--label-white);
    border: 2px solid var(--label-edge);
    display: flex;
    flex-direction: column;
    align-items: center;
    justify-content: center;
    text-align: center;
    color: var(--ink);
    padding: 0 70px;
  }
  .side-label {
    position: absolute;
    left: 200px;
    top: 730px;
    width: 800px;
    height: 400px;
    border-radius: 24px;
    background: var(--label-white);
    border: 2px solid var(--label-edge);
    display: flex;
    flex-direction: column;
    align-items: center;
    justify-content: center;
    text-align: center;
    color: var(--ink);
  }
  .wordmark {
    font-family: "Playfair Display", Georgia, serif;
    font-weight: 800;
    line-height: 1;
    letter-spacing: 4px;
    color: var(--ink);
  }
  .lid-label .wordmark {
    font-size: 112px;
    margin-top: -10px;
  }
  .side-label .wordmark {
    font-size: 136px;
  }
  .product-name {
    font-family: "Montserrat", Arial, sans-serif;
    font-weight: 700;
    letter-spacing: 5px;
  }
  .lid-label .product-name {
    font-size: 31px;
    margin-top: 12px;
  }
  .side-label .product-name {
    font-size: 38px;
    margin-top: 16px;
  }
  .scent {
    font-family: "Montserrat", Arial, sans-serif;
    font-weight: 700;
    font-size: 25px;
    letter-spacing: 4px;
    margin-top: 22px;
  }
  .hold-finish {
    font-family: "Montserrat", Arial, sans-serif;
    font-weight: 500;
    font-size: 18px;
    letter-spacing: 2.5px;
    margin-top: 12px;
  }
  .net-weight {
    font-family: "Montserrat", Arial, sans-serif;
    font-weight: 500;
    font-size: 21px;
    letter-spacing: 3px;
    margin-top: 34px;
  }
</style>
</head>
<body>
  <main class="canvas">
    <section class="lid-label">
      <h1 class="wordmark">BRANT</h1>
      <p class="product-name">HAIR POMADE</p>
      <p class="scent">FRESH &amp; CLEAN</p>
      <p class="hold-finish">MEDIUM HOLD – MATTE FINISH</p>
      <p class="net-weight">NET WT 2 oz (57 g)</p>
    </section>
    <section class="side-label">
      <p class="wordmark">BRANT</p>
      <p class="product-name">HAIR POMADE</p>
    </section>
  </main>
</body>
</html>
```